Car rental website design for a UAE car rental company

This project is about creating a new website design for a car rental company located in Dubai (United Arab Emirates), I opened the same project a few months ago but I didn't receive a lot of appealing entries so I closed it but this time I am marking the project as guaranteed to avoid such situation again, if you have already provided a design before then please re-submit again on this project so that it is considered while reviewing all the designs

A few important things:

1- We need a simple non-complex design
2- The final deliverable would be 2 screens (PSD, JPEG ... etc), the first screen is for the home page and the second screen is for an internal page
3- The home page must have a section that end users can use to rent a car online directly from the home page instead of going into some inner pages
4- The current website is very old and not very appealing so avoid creating a similar design (www.quarvin-drive.example)
5- The name is Quarvin but the company rents normal cars (no Limousin cars will be rented) so avoid adding any fancy cars in the images/graphics used in the design, just normal end users cars
6- The expected pages would be: home, About us, Our team, Strategy, Contact us and links to social media pages
7- The attachments include the company's logo and some screens from other car rental companies that provide online rentals/payments

If you have any questions please feel free to ask and please note that we will need the designs urgently

Thanks

Target Market(s)

Dubai - United Arab Emirates

Industry/Entity Type

It Company

Number of Pages Required

2 page

Font styles to use
Sans Serif

Requirements
Must have
• Check the project details
Nice to have
Should not have

```html
<!DOCTYPE html>
<html lang="en">
<head>
<meta charset="utf-8">
<title>Quarvin — Car Rental Dubai</title>
<link rel="stylesheet" href="https://fonts.googleapis.com/css2?family=Open+Sans:wght@400;600;700&family=Source+Sans+3:wght@400;600&display=swap">
<style>
:root{
  --crimson:#a3002f;
  --crimson-dark:#8a0027;
  --sky-mid:#7fa9cf;
  --sky-low:#c9dcea;
  --road:#3b4045;
  --tab-grey:#b8c2b4;
  --panel:#e3edf3;
  --ink:#222;
  --muted:#e9a9b9;
  --line:#e3ece6;
  --white:#fff;
}
*{box-sizing:border-box;margin:0;padding:0}
html,body{width:1200px;height:1050px;overflow:hidden;background:var(--white)}
body{position:relative;font-family:"Open Sans",Arial,sans-serif;color:var(--ink)}
.hero{position:absolute;left:0;top:0;width:1200px;height:437px;
  background:linear-gradient(180deg,#1d3b58 0,#2f5a82 96px,var(--sky-mid) 200px,var(--sky-low) 300px,#8d98a0 345px,#6f9a5c 365px,var(--road) 380px,#2d3236 437px);
  border-bottom:3px solid var(--crimson)}
.hero-scene{position:absolute;left:690px;top:250px;width:380px;height:180px;border-radius:60px 60px 14px 14px;
  background:linear-gradient(160deg,#b9c2c9,#8a96a0 60%,#6a4a56);opacity:.85}
.topbar{position:absolute;top:6px;left:660px;display:flex;align-items:center;gap:10px;font-size:12px;color:var(--white)}
.topbar .phone{display:flex;align-items:center;gap:6px;margin-right:8px}
.account{background:#24313b;border-radius:3px;padding:2px 10px;display:flex;gap:8px;align-items:center;font-size:11px}
.account small{font-size:9px}
.brand{position:absolute;left:225px;top:32px;display:flex;align-items:center;gap:8px}
.brand-mark{width:30px;height:30px;background:var(--crimson)}
.brand-name{font-family:"Source Sans 3",sans-serif;font-size:24px;font-weight:600;color:var(--white)}
.main-nav{position:absolute;left:508px;top:54px;display:flex;list-style:none;gap:2px}
.main-nav li{transform:skewX(-25deg);background:var(--tab-grey);height:31px;padding:0 22px;display:flex;align-items:center}
.main-nav li span{transform:skewX(25deg);font-size:12px;font-weight:600;color:#1a1a1a}
.main-nav li.active{background:var(--crimson)}
.main-nav li.active span{color:var(--white)}
.booking{position:absolute;left:225px;top:134px;width:294px;height:251px;background:rgba(227,237,243,.92)}
.booking-tabs{display:flex;height:29px}
.booking-tabs div{flex:1;display:flex;align-items:center;justify-content:center;font-size:12px}
.booking-tabs .on{color:var(--crimson);border-top:3px solid var(--crimson);background:var(--panel)}
.booking-tabs .off{background:#a7b2ab;color:#222}
.booking-body{padding:12px 24px 0}
.lbl{font-size:8px;color:#444;display:flex;justify-content:space-between}
.lbl u{color:#444}
.field{background:var(--white);border:1px solid #cfd8dd;border-radius:3px;height:30px;font-size:8px;color:#999;display:flex;align-items:center;padding-left:10px;margin-top:4px}
.check{display:flex;align-items:center;gap:6px;font-size:8px;margin:8px 0 14px}
.check i{width:14px;height:14px;background:var(--white);border:1px solid #cfd8dd;border-radius:2px}
.row{display:flex;gap:8px}
.col{display:flex;flex-direction:column}
.row-end{display:flex;justify-content:space-between;align-items:flex-end;margin-top:12px}
.select{width:75px;height:30px;background:var(--white);border:1px solid #cfd8dd;border-radius:3px;font-size:8px;color:#777;display:flex;align-items:center;justify-content:space-between;padding:0 8px;margin-top:4px}
.btn{background:var(--crimson);color:var(--white);border-radius:3px;font-size:10px;font-weight:700;display:flex;align-items:center;justify-content:center;gap:6px}
.section-head{height:41px;background:repeating-linear-gradient(45deg,#f4f4f4 0 2px,#fafafa 2px 4px);
  font-family:"Source Sans 3",sans-serif;font-size:21px;font-weight:400;color:var(--crimson);display:flex;align-items:center;padding-left:12px}
.features{position:absolute;left:225px;top:458px;width:456px}
.car-grid{display:grid;grid-template-columns:224px 224px;gap:8px;margin-top:14px}
.car-card{height:129px;border:3px solid var(--line);position:relative}
.car-photo{position:absolute;left:9px;top:9px;width:113px;height:74px;background:linear-gradient(180deg,#9fb7c9,#5c7a4f)}
.car-info{position:absolute;left:128px;top:7px;width:85px}
.car-info h3{font-size:11px;font-weight:400;color:var(--crimson);border-bottom:1px solid var(--crimson);padding-bottom:1px}
.car-info p{font-size:8px;margin-top:3px;white-space:nowrap}
.price{position:absolute;left:128px;top:65px;font-size:12px}
.car-meta{position:absolute;left:9px;top:90px;font-size:9px;line-height:15px}
.car-card .btn{position:absolute;left:128px;top:90px;width:84px;height:26px;font-weight:400}
.services{position:absolute;left:700px;top:458px;width:275px;height:320px;background:var(--crimson);color:var(--white);padding:12px 18px}
.panel-title{font-family:"Source Sans 3",sans-serif;font-size:17px;font-weight:600;border-bottom:1px solid var(--white);padding-bottom:3px}
.services ul{list-style:none;margin-top:14px}
.services li{margin-bottom:12px}
.services h4{font-size:10px;font-weight:400;display:flex;gap:10px;align-items:center}
.services h4::before{content:"";border-left:5px solid var(--white);border-top:3px solid transparent;border-bottom:3px solid transparent}
.services p{font-size:9px;color:var(--muted);line-height:14px;margin-top:3px}
.read-more{font-size:9px;text-align:right;color:var(--muted)}
.welcome{position:absolute;left:225px;top:797px;width:456px}
.welcome .body{font-size:10.5px;line-height:16px;margin-top:20px}
.welcome .body p{margin-bottom:14px}
.welcome .read-more{color:var(--crimson);margin-top:-6px}
.mission{position:absolute;left:700px;top:797px;width:275px;height:188px;background:var(--crimson);color:var(--white);padding:10px 18px}
.mission-photo{margin-top:10px;height:66px;background:linear-gradient(120deg,#e6e9ec,#aab3bb 60%,#c9a38c)}
.mission p{font-size:9px;line-height:14px;margin-top:8px}
.footer{position:absolute;left:0;top:985px;width:1200px;height:38px;background:var(--crimson);border-top:3px solid var(--crimson-dark)}
.footer-nav{position:absolute;left:225px;top:12px;display:flex;gap:14px;font-size:9px;color:var(--white);list-style:none}
.footer-nav li+li::before{content:"|";margin-right:14px}
.social{position:absolute;left:790px;top:1002px;display:flex;gap:6px}
.social i{width:28px;height:28px;border-radius:50%;border:2px solid var(--white);background:var(--crimson)}
.copyright{position:absolute;top:1031px;width:1200px;text-align:center;font-size:8px;color:var(--crimson)}
</style>
</head>
<body>

<div class="hero" role="img" aria-label="Sky over a city skyline with a grassy verge and road"></div>
<div class="hero-scene" role="img" aria-label="Silver family SUV with luggage and travellers"></div>

<div class="topbar">
  <span class="phone">
    <svg width="14" height="12" viewBox="0 0 14 12"><path d="M1 4c0-2 2-3 6-3s6 1 6 3v1h-3V3.5H4V5H1z M3 6h8l1 5H2z" fill="#fff"/></svg>
    +971 455 0192
  </span>
  <span class="account">LOGIN &nbsp;| <small>Not a member yet ?</small> SIGN UP</span>
  <svg width="13" height="13" viewBox="0 0 13 13"><circle cx="5" cy="5" r="4" fill="none" stroke="#fff" stroke-width="1.6"/><path d="M8 8l4 4" stroke="#fff" stroke-width="2"/></svg>
</div>

<div class="brand"><span class="brand-mark"></span><span class="brand-name">Quarvin</span></div>

<ul class="main-nav">
  <li class="active"><span>HOME</span></li>
  <li><span>ABOUT US</span></li>
  <li><span>OUR TEAM</span></li>
  <li><span>STRATEGY</span></li>
  <li><span>CONTACT US</span></li>
</ul>

<form class="booking">
  <div class="booking-tabs"><div class="on">Book a Car</div><div class="off">Manage Reservation</div></div>
  <div class="booking-body">
    <div class="lbl"><span>LOCATION</span><u>AIRPORT CODES</u></div>
    <div class="field">Enter airport, city or zip code</div>
    <div class="check"><i></i>Return at different location</div>
    <div class="row">
      <div class="col"><span class="lbl">PICK-UP DATE</span><div class="field" style="width:78px">▦</div></div>
      <div class="col"><span class="lbl">TIME</span><div class="field" style="width:37px"></div></div>
      <div class="col"><span class="lbl">DROP-OFF DATE</span><div class="field" style="width:78px">▦</div></div>
      <div class="col"><span class="lbl">TIME</span><div class="field" style="width:37px"></div></div>
    </div>
    <div class="row-end">
      <div class="col"><span class="lbl">CAR TYPE</span><div class="select">Standard <span>▾</span></div></div>
      <div class="btn" style="width:76px;height:30px">CONTINUE <span>›</span></div>
    </div>
  </div>
</form>

<section class="features">
  <h2 class="section-head">Feature Cars</h2>
  <div class="car-grid">
    <article class="car-card">
      <div class="car-photo" role="img" aria-label="White convertible parked on grass"></div>
      <div class="car-info"><h3>2006 Veltro</h3><p>V-Series 240e Sedan</p></div>
      <div class="price">$12.00</div>
      <div class="car-meta">Mileage: 50,000<br>Stock Number: 118755</div>
      <div class="btn">View Details</div>
    </article>
    <article class="car-card">
      <div class="car-photo" role="img" aria-label="Dark convertible in front of trees"></div>
      <div class="car-info"><h3>2006 Veltro</h3><p>V-Series 240e Sedan</p></div>
      <div class="price">$12.00</div>
      <div class="car-meta">Mileage: 50,000<br>Stock Number: 118755</div>
      <div class="btn">View Details</div>
    </article>
    <article class="car-card">
      <div class="car-photo" role="img" aria-label="Red coupe under a blue sky" style="background:linear-gradient(180deg,#8fb4d9,#b0334a 70%,#777)"></div>
      <div class="car-info"><h3>2006 Veltro</h3><p>V-Series 240e Sedan</p></div>
      <div class="price">$12.00</div>
      <div class="car-meta">Mileage: 50,000<br>Stock Number: 118755</div>
      <div class="btn">View Details</div>
    </article>
    <article class="car-card">
      <div class="car-photo" role="img" aria-label="Navy convertible on a country road" style="background:linear-gradient(180deg,#7d9b5a,#1f2c4d 70%,#8a8a6a)"></div>
      <div class="car-info"><h3>2006 Veltro</h3><p>V-Series 240e Sedan</p></div>
      <div class="price">$12.00</div>
      <div class="car-meta">Mileage: 50,000<br>Stock Number: 118755</div>
      <div class="btn">View Details</div>
    </article>
  </div>
</section>

<aside class="services">
  <h2 class="panel-title">Services</h2>
  <ul>
    <li><h4>Maintenance &amp; Repair</h4><p>Lorem Ipsum is simply dummy text of the printing and typesetting industry.</p></li>
    <li><h4>Schedule a Service</h4><p>Lorem Ipsum is simply dummy text of the printing and typesetting industry. Lorem Ipsum has been the industry's standard dummy text ever since the 1500s.</p></li>
    <li><h4>Parts &amp; Accessories</h4><p>Lorem Ipsum is simply dummy text of the printing and typesetting industry lorem Ipsum.</p></li>
    <li><h4>Service Specials</h4><p>Lorem Ipsum is simply dummy text of the printing and typesetting industry.</p></li>
  </ul>
  <p class="read-more">read more [+]</p>
</aside>

<section class="welcome">
  <h2 class="section-head">Welcome to Quarvin</h2>
  <div class="body">
    <p>As Dubai is expected to welcome millions of tourists and visitors, car rental industry is believed to escalate more rapidly in the region.</p>
    <p>Over the past five years, demands for car rentals in Dubai has been augmenting at a healthy pace and is currently registering a growth rate of 20 to 25 percent per year. The swift economic growth and the number.....</p>
  </div>
  <p class="read-more">read more [+]</p>
</section>

<aside class="mission">
  <h2 class="panel-title">Mission &amp; Vision</h2>
  <div class="mission-photo" role="img" aria-label="Hand passing car keys in front of a silver car"></div>
  <p>To be one of the leading auto leasing company in the fast growing economy and tourism industry of the emirate of Dubai and play alongside....</p>
  <p class="read-more" style="margin-top:2px">read more [+]</p>
</aside>

<footer class="footer">
  <ul class="footer-nav"><li>Home</li><li>About Us</li><li>Our Team</li><li>Strategy</li><li>Contact Us</li></ul>
</footer>
<div class="social" aria-label="Social media links"><i></i><i></i><i></i><i></i><i></i></div>
<p class="copyright">© Copyright 2015, Quarvin. All rights reserved.</p>

</body>
</html>
```